KerrLow Farm

Need a nice simple clean double sided business card that has our logo and info on:
Kerr Low Farm
Martin & Felicity Kerr Low
kerrlowfarm@mailbarn.example
Martin: 1-780-555-0148
Felicity: 1-780-555-0193
Instagram @ kerrlow_farm

Contact Information for Business Card

Martin & Felicity Kerr Low kerrlowfarm@mailbarn.example Martin: 1-780-555-0148 Felicity: 1-780-555-0193

```html
<!DOCTYPE html>
<html lang="en">
<head>
<meta charset="utf-8">
<title>Kerr Low Farm – Business Card</title>
<link rel="stylesheet" href="https://fonts.googleapis.com/css2?family=EB+Garamond:wght@500;700&family=Arimo:wght@400&display=swap">
<style>
  :root {
    --page-bg: #b4b7b8;
    --farm-green: #4f9a3d;
    --card-green: #4b9340;
    --deep-green: #3b7a31;
    --emboss-green: #3f7f35;
    --wheat-orange: #f4a32c;
    --text-green: #3b8a2e;
    --card-white: #ffffff;
  }
  * { box-sizing: border-box; margin: 0; padding: 0; }
  html, body { width: 1200px; height: 928px; overflow: hidden; }
  body { background: var(--page-bg); position: relative; font-family: "Arimo", sans-serif; }

  .card {
    position: absolute;
    left: 265px;
    width: 670px;
    height: 383px;
    border-radius: 14px;
    overflow: hidden;
  }

  /* Back side */
  .card--back { top: 58px; background: var(--card-green); }
  .back-mark {
    position: absolute; left: 273px; top: 99px;
    width: 124px; height: 124px;
    border: 3px solid var(--emboss-green); border-radius: 50%;
  }
  .back-name {
    position: absolute; left: 0; right: 0; top: 228px;
    text-align: center;
    font-family: "EB Garamond", serif; font-weight: 500;
    font-size: 35px; color: var(--emboss-green); letter-spacing: 0.5px;
  }
  .back-tagline {
    position: absolute; left: 0; right: 0; top: 272px;
    text-align: center; font-size: 13px; letter-spacing: 6.5px;
    color: var(--emboss-green);
  }

  /* Front side */
  .card--front { top: 485px; background: var(--card-white); }
  .front-mark {
    position: absolute; left: 112px; top: 24px;
    width: 99px; height: 99px;
    border: 3px solid var(--farm-green); border-radius: 50%;
  }
  .front-name {
    position: absolute; left: 34px; top: 127px; width: 260px;
    text-align: center;
    font-family: "EB Garamond", serif; font-weight: 500;
    font-size: 30px; line-height: 1; color: var(--farm-green);
  }
  .front-tagline {
    position: absolute; left: 34px; top: 161px; width: 260px;
    text-align: center; font-size: 11.5px; letter-spacing: 6px;
    color: var(--wheat-orange);
  }
  .owners {
    position: absolute; right: 34px; top: 37px;
    font-family: "EB Garamond", serif; font-weight: 700;
    font-size: 19px; color: var(--text-green);
  }
  .owners .surname { color: var(--wheat-orange); }

  .contact-list {
    position: absolute; left: 34px; top: 229px; list-style: none;
  }
  .contact-list li {
    display: flex; align-items: center; gap: 11px;
    height: 24px; font-size: 15px; color: var(--text-green); letter-spacing: 0.3px;
  }
  .contact-icon { width: 13px; height: 13px; flex: none; }

  .wheat-art {
    position: absolute; left: 452px; top: 125px;
    width: 100px; height: 210px;
    background: linear-gradient(180deg, rgba(244,163,44,0.85), rgba(244,163,44,0.55) 65%, rgba(79,154,61,0.6));
    border-radius: 50px 50px 8px 8px;
  }
  .ground-wave { position: absolute; left: 0; bottom: 0; width: 670px; height: 70px; }
</style>
</head>
<body>

<section class="card card--back" aria-label="Card back">
  <div class="back-mark"></div>
  <div class="back-name">KERR LOW FARM</div>
  <div class="back-tagline">STONE MILLED FLOUR</div>
</section>

<section class="card card--front" aria-label="Card front">
  <div class="front-mark"></div>
  <div class="front-name">KERR LOW FARM</div>
  <div class="front-tagline">STONE MILLED FLOUR</div>

  <div class="owners">Martin &amp; Felicity <span class="surname">Kerr Low</span></div>

  <ul class="contact-list">
    <li>
      <svg class="contact-icon" viewBox="0 0 16 16"><path fill="var(--wheat-orange)" d="M3.6 1.2l2.3 2.4-1.3 2c.9 2 2.6 3.7 4.7 4.7l2-1.3 2.4 2.3-1.4 2.5C6.5 13.6 2.1 9.2 1.2 3.2z"/></svg>
      <span>1-780-555-0148 (Martin)</span>
    </li>
    <li>
      <svg class="contact-icon" viewBox="0 0 16 16"><path fill="var(--wheat-orange)" d="M3.6 1.2l2.3 2.4-1.3 2c.9 2 2.6 3.7 4.7 4.7l2-1.3 2.4 2.3-1.4 2.5C6.5 13.6 2.1 9.2 1.2 3.2z"/></svg>
      <span>1-780-555-0193 (Felicity)</span>
    </li>
    <li>
      <svg class="contact-icon" viewBox="0 0 16 16"><rect x="1" y="3" width="14" height="10" fill="var(--wheat-orange)"/><path d="M1.5 3.5L8 8.5l6.5-5" fill="none" stroke="#fff" stroke-width="1.4"/></svg>
      <span>kerrlowfarm@mailbarn.example</span>
    </li>
    <li>
      <svg class="contact-icon" viewBox="0 0 16 16"><rect x="2" y="2" width="12" height="12" rx="2" fill="none" stroke="var(--wheat-orange)" stroke-width="1.8"/></svg>
      <span>@kerrlow_farm</span>
    </li>
  </ul>

  <div class="wheat-art" role="img" aria-label="Illustration of two golden wheat stalks with green leaves"></div>

  <svg class="ground-wave" viewBox="0 0 670 70" preserveAspectRatio="none" aria-hidden="true">
    <path d="M0 37 C120 50 250 46 380 28 C470 16 540 12 600 18 C630 22 650 26 670 30 L670 70 L0 70 Z" fill="var(--wheat-orange)"/>
    <path d="M0 45 C130 56 260 52 390 33 C480 21 550 18 610 25 C640 29 655 33 670 37 L670 70 L0 70 Z" fill="#ffffff"/>
    <path d="M0 48 C130 59 260 56 390 37 C480 25 550 22 610 29 C640 33 655 37 670 41 L670 70 L0 70 Z" fill="var(--farm-green)"/>
  </svg>
</section>

</body>
</html>
```